Tidewell Recovery Business Card Design

Professional and clean design. The design colors should flow with the logo. Two-sided card with the website on the back which is:

www.TidewellRecovery.example.

"Specializing in Water Damage Restoration"

On the front I need the name, email, phone, and logo.

Name: Dorian Vashti
Email: Dorian@TidewellRecovery.example
Phone: 555-318-2046 for now

I only have the Preview and Thumbnail right now but should have the source files uploaded within a day or two.

Target Market(s)

Flood victims, home owners with water damage from busted pipes etc...

Industry/Entity Type

Business

Contact Information for Business Card

Name: Dorian Vashti

Font styles to use
Serif
Sans Serif

```html
<!DOCTYPE html>
<html lang="en">
<head>
<meta charset="utf-8">
<title>Tidewell Recovery – Business Card</title>
<link rel="stylesheet" href="https://fonts.googleapis.com/css2?family=Cinzel:wght@600&family=Cormorant+Garamond:ital,wght@1,700&family=Fira+Sans+Condensed:ital,wght@0,500;1,500&display=swap">
<style>
  :root {
    --sky: #5bbfea;
    --ocean: #2f95d3;
    --ink: #2e8fd0;
    --paper: #ffffff;
    --backdrop: #eef1f4;
  }
  html, body {
    margin: 0;
    padding: 0;
    width: 960px;
    height: 1200px;
    overflow: hidden;
    background: var(--backdrop);
  }
  .canvas {
    position: relative;
    width: 960px;
    height: 1200px;
  }
  .card {
    position: absolute;
    left: 100px;
    width: 761px;
    height: 444px;
    background: var(--paper);
    box-shadow: 0 10px 18px rgba(0,0,0,0.18);
  }
  .card--front { top: 82px; }
  .card--back { top: 656px; }
  .card svg { display: block; width: 761px; height: 444px; }
  .fill-sky { fill: var(--sky); }
  .fill-ocean { fill: var(--ocean); }
  .holder-name {
    font-family: "Cormorant Garamond", Georgia, serif;
    font-style: italic;
    font-weight: 700;
    font-size: 46px;
    letter-spacing: 1px;
    fill: var(--ink);
  }
  .contact-line {
    font-family: "Fira Sans Condensed", "Arial Narrow", sans-serif;
    font-style: italic;
    font-weight: 500;
    font-size: 22px;
    fill: var(--ink);
  }
  .icon { fill: var(--ink); }
  .icon-line { fill: none; stroke: var(--ink); stroke-width: 2.4; }
  .wordmark {
    font-family: "Cinzel", Georgia, serif;
    font-weight: 600;
    fill: var(--ink);
  }
  .wordmark--front { font-size: 28px; letter-spacing: 1px; }
  .wordmark--back { font-size: 19px; letter-spacing: 0.5px; }
  .mark-ring { fill: var(--paper); stroke: var(--ocean); stroke-width: 10; }
  .mark-dot { fill: var(--sky); }
  .back-site {
    font-family: "Fira Sans Condensed", "Arial Narrow", sans-serif;
    font-weight: 500;
    font-size: 38px;
    fill: var(--ink);
  }
</style>
</head>
<body>
<main class="canvas">

  <section class="card card--front" aria-label="Business card front">
    <svg viewBox="0 0 951 555" xmlns="http://www.w3.org/2000/svg">
      <path class="fill-sky" d="M0,0 H951 V272 C700,120 400,30 0,35 Z"/>
      <path class="fill-ocean" d="M0,35 C400,30 700,120 951,272 L951,280 C700,140 400,58 0,58 Z"/>

      <text class="holder-name" x="64" y="174">DORIAN VASHTI</text>

      <g class="contact-phone">
        <path class="icon" d="M70,216 l9,-2 l6,14 l-6,5 c3,8 9,14 17,18 l5,-6 l14,6 l-2,9 c-2,4 -6,5 -10,4 c-18,-5 -32,-19 -37,-37 c-1,-4 0,-9 4,-11 z"/>
        <text class="contact-line" x="139" y="245">555-318-2046</text>
      </g>

      <g class="contact-email">
        <rect class="icon" x="65" y="331" width="42" height="29"/>
        <path d="M67,333 L86,349 L105,333 M67,358 L81,346 M105,358 L91,346" fill="none" stroke="#fff" stroke-width="2"/>
        <text class="contact-line" x="139" y="357">Dorian@TidewellRecovery.example</text>
      </g>

      <g class="contact-web">
        <circle class="icon-line" cx="86" cy="443" r="22"/>
        <ellipse class="icon-line" cx="86" cy="443" rx="10" ry="22"/>
        <path class="icon-line" d="M86,421 V465 M64,443 H108 M68,432 H104 M68,454 H104"/>
        <text class="contact-line" x="139" y="452">www.TidewellRecovery.example</text>
      </g>

      <g class="brand-block">
        <circle class="mark-ring" cx="714" cy="297" r="88"/>
        <circle class="mark-dot" cx="714" cy="297" r="60"/>
        <text class="wordmark wordmark--front" x="714" y="440" text-anchor="middle">TIDEWELL RECOVERY</text>
      </g>

      <rect class="fill-sky" x="0" y="487" width="951" height="23"/>
    </svg>
  </section>

  <section class="card card--back" aria-label="Business card back">
    <svg viewBox="0 0 951 555" xmlns="http://www.w3.org/2000/svg">
      <text class="back-site" x="475" y="232" text-anchor="middle">www.TidewellRecovery.example</text>

      <path class="fill-ocean" d="M0,312 C150,295 300,330 500,400 S800,510 951,497 V555 H0 Z"/>
      <path class="fill-sky" d="M0,375 C150,358 330,385 520,440 S820,540 951,518 V555 H0 Z"/>

      <g class="brand-block">
        <circle class="mark-ring" cx="822" cy="392" r="74"/>
        <text class="wordmark wordmark--back" x="822" y="388" text-anchor="middle">TIDEWELL</text>
        <text class="wordmark wordmark--back" x="822" y="412" text-anchor="middle">RECOVERY</text>
      </g>
    </svg>
  </section>

</main>
</body>
</html>
```